VelnoraTek Bright IT Consultancy
All Stationary + ESignaure + Powerpoint Template
Simple
Tomás Barrena Ollé
President & CEO
3er Cjon Calle Fresal 57
Las Brisas, Valdoro
Ciudad Alcena, 07215
See additional comments
tomas.barrena@velnoratek.mx
www.velnoratek.com.mx
I dont have a permanent local phone number yet, so I dont want to give an informal impression about the company, so Designers I need your creativite to avoid that impression something as simple as "cell&phone" but with all your experience and creativity, an special cell+phone logo for example. Other request is a clean, simple, modern, corporate and professional material.
Go Bright...Go Sky
Go Sky...& Connect
Share...& Succed
Logo Velno
Logo Velno 2
Logo 3
Logo 4
This is an example of standard bullets and numbers in a powerpoint presentation

```html
<!DOCTYPE html>
<html lang="en">
<head>
<meta charset="utf-8">
<title>VelnoraTek Bright IT Consultancy — Stationery and Presentation</title>
<link href="https://fonts.googleapis.com/css2?family=Open+Sans:wght@400;600&display=swap" rel="stylesheet">
<style>
  :root {
    --bg: #e9eaeb;
    --paper: #ffffff;
    --brand: #1f5f8b;
    --brand-light: #4f8fb8;
    --accent: #7fb23a;
    --text: #5a5f63;
    --muted: #9aa0a4;
    --dark-card: #5d6266;
    --shadow: 0 1px 3px rgba(0,0,0,.18);
  }
  * { box-sizing: border-box; margin: 0; padding: 0; }
  html, body { width: 1200px; height: 378px; overflow: hidden; }
  body {
    background: var(--bg);
    font-family: "Open Sans", Arial, sans-serif;
    color: var(--text);
    position: relative;
  }
  .sheet { position: absolute; background: var(--paper); box-shadow: var(--shadow); overflow: hidden; }

  /* brand name lockup */
  .brand { display: flex; align-items: center; gap: 4px; color: var(--brand); font-weight: 600; white-space: nowrap; }
  .brand-dot { border-radius: 50%; background: var(--brand); flex: none; }
  .brand.sm { font-size: 7px; } .brand.sm .brand-dot { width: 6px; height: 6px; }
  .brand.md { font-size: 10px; } .brand.md .brand-dot { width: 8px; height: 8px; }
  .brand.lg { font-size: 20px; gap: 7px; } .brand.lg .brand-dot { width: 16px; height: 16px; }
  .brand.light { color: #ffffff; } .brand.light .brand-dot { background: #ffffff; }

  .pattern-fill { position: absolute; background: radial-gradient(circle at 70% 70%, rgba(79,143,184,.35), rgba(127,178,58,.12) 55%, rgba(255,255,255,0) 80%); }

  /* letterhead */
  .letterhead { left: 12px; top: 12px; width: 216px; height: 252px; }
  .letterhead .brand { position: absolute; left: 18px; top: 20px; }
  .letterhead .pattern-fill { right: 0; bottom: 0; width: 110px; height: 110px; }
  .letterhead .footer { position: absolute; left: 18px; bottom: 10px; font-size: 4px; color: var(--muted); line-height: 1.4; }

  /* cover */
  .cover { left: 252px; top: 12px; width: 206px; height: 252px; }
  .cover .brand { position: absolute; left: 50%; top: 100px; transform: translateX(-50%); }
  .cover .tagline { position: absolute; width: 100%; top: 128px; text-align: center; font-size: 6px; color: var(--muted); letter-spacing: .5px; }

  /* business cards */
  .card { width: 106px; height: 38px; left: 496px; }
  .card .brand { position: absolute; left: 7px; top: 7px; }
  .card .details { position: absolute; right: 6px; bottom: 4px; text-align: right; font-size: 3.4px; line-height: 1.35; color: var(--text); }
  .card .details strong { color: var(--brand); font-weight: 600; }
  .card.front { top: 130px; }
  .card.back { top: 174px; }
  .card.back .brand { left: 50%; top: 50%; transform: translate(-50%,-50%); }

  .mini-card { left: 12px; width: 88px; height: 42px; }
  .mini-card.one { top: 272px; }
  .mini-card.one .brand { position: absolute; left: 7px; top: 17px; }
  .mini-card.two { top: 320px; }
  .mini-card.two .details { position: absolute; left: 7px; top: 10px; font-size: 3.4px; line-height: 1.4; }

  /* envelope */
  .envelope { left: 112px; top: 272px; width: 370px; height: 90px; }
  .envelope .band { position: absolute; left: 0; right: 0; top: 0; height: 18px; background: var(--brand-light); display: flex; align-items: center; justify-content: center; color: #fff; font-size: 5px; letter-spacing: 1px; }
  .envelope .brand { position: absolute; left: 12px; bottom: 12px; }
  .envelope .address { position: absolute; left: 170px; top: 46px; font-size: 4px; line-height: 1.4; }

  .dark-card { left: 496px; width: 106px; height: 42px; background: var(--dark-card); }
  .dark-card.one { top: 272px; }
  .dark-card.two { top: 320px; }
  .dark-card .brand { position: absolute; left: 7px; top: 17px; }
  .dark-card .pattern-fill { right: 0; top: 0; width: 50px; height: 42px; background: linear-gradient(90deg, rgba(255,255,255,0), rgba(127,178,58,.35)); }

  /* slides */
  .slide { width: 156px; height: 112px; }
  .slide h3 { position: absolute; left: 8px; top: 8px; font-size: 6px; font-weight: 600; color: var(--brand); white-space: nowrap; }
  .slide p, .slide li { font-size: 3.8px; line-height: 1.5; color: var(--text); }
  .slide .body { position: absolute; left: 8px; top: 22px; right: 8px; }
  .slide ul, .slide ol { padding-left: 8px; }
  .slide .pattern-fill { right: 0; bottom: 0; width: 50px; height: 50px; }

  .slide.title { top: 10px; }
  .slide.title .brand { position: absolute; left: 10px; top: 14px; }
  .slide.title .heading { position: absolute; left: 10px; top: 42px; font-size: 6px; color: var(--brand); line-height: 1.3; }
  .slide.title .heading b { font-weight: 600; }
  .slide.title .sub { position: absolute; left: 10px; top: 64px; font-size: 4px; color: var(--muted); }
  .slide.title .pattern-fill { width: 64px; height: 76px; top: 10px; bottom: auto; }

  .col-a { left: 684px; } .col-b { left: 848px; } .col-c { left: 1012px; }
  .row-1 { top: 132px; } .row-2 { top: 256px; }
  .welcome { left: 770px; } .thanks { left: 934px; }

  .image-slot { position: absolute; background: linear-gradient(135deg, #cfd9e2, #e6ecf1); }
  .chart { position: absolute; left: 20px; top: 24px; }
</style>
</head>
<body>

  <section class="sheet letterhead">
    <div class="brand md"><span class="brand-dot"></span>VelnoraTek</div>
    <div class="pattern-fill" role="img" aria-label="Soft decorative dot pattern in blue and green"></div>
    <div class="footer">3er Cjon Calle Fresal 57, Las Brisas, Valdoro, Ciudad Alcena, 07215<br>tomas.barrena@velnoratek.mx · www.velnoratek.com.mx</div>
  </section>

  <section class="sheet cover">
    <div class="brand lg"><span class="brand-dot"></span>VelnoraTek</div>
    <div class="tagline">Bright IT Consultancy</div>
  </section>

  <section class="sheet card front">
    <div class="brand sm"><span class="brand-dot"></span>VelnoraTek</div>
    <div class="details"><strong>Tomás Barrena Ollé</strong><br>President &amp; CEO<br>3er Cjon Calle Fresal 57, Las Brisas<br>tomas.barrena@velnoratek.mx</div>
  </section>
  <section class="sheet card back">
    <div class="brand md"><span class="brand-dot"></span>VelnoraTek</div>
  </section>

  <section class="sheet mini-card one">
    <div class="brand sm"><span class="brand-dot"></span>VelnoraTek</div>
  </section>
  <section class="sheet mini-card two">
    <div class="details">Tomás Barrena Ollé<br>President &amp; CEO<br>tomas.barrena@velnoratek.mx<br>www.velnoratek.com.mx</div>
  </section>

  <section class="sheet envelope">
    <div class="band">www.velnoratek.com.mx</div>
    <div class="brand sm"><span class="brand-dot"></span>VelnoraTek</div>
    <div class="address">3er Cjon Calle Fresal 57<br>Las Brisas, Valdoro<br>Ciudad Alcena, 07215</div>
  </section>

  <section class="sheet dark-card one">
    <div class="brand sm light"><span class="brand-dot"></span>VelnoraTek</div>
    <div class="pattern-fill" role="img" aria-label="Soft decorative dot pattern"></div>
  </section>
  <section class="sheet dark-card two">
    <div class="brand sm light"><span class="brand-dot"></span>VelnoraTek</div>
    <div class="pattern-fill" role="img" aria-label="Soft decorative dot pattern"></div>
  </section>

  <section class="sheet slide title welcome">
    <div class="brand sm"><span class="brand-dot"></span>VelnoraTek</div>
    <div class="heading">Welcome to Our<br><b>Presentation Name</b></div>
    <div class="sub">Name Here</div>
    <div class="pattern-fill" role="img" aria-label="Soft decorative dot pattern"></div>
  </section>
  <section class="sheet slide title thanks">
    <div class="brand sm"><span class="brand-dot"></span>VelnoraTek</div>
    <div class="heading"><b>Thanks</b></div>
    <div class="sub">See you soon</div>
    <div class="pattern-fill" role="img" aria-label="Soft decorative dot pattern"></div>
  </section>

  <section class="sheet slide col-a row-1">
    <h3>Heading Here</h3>
    <div class="body"><p>Add your text here to describe this point</p></div>
    <div class="pattern-fill" role="img" aria-label="Soft decorative dot pattern"></div>
  </section>
  <section class="sheet slide col-b row-1">
    <h3>Heading Here</h3>
    <div class="image-slot" style="left:8px;top:24px;width:60px;height:52px" role="img" aria-label="Placeholder for a slide image"></div>
    <div class="body" style="left:76px"><p>Short caption goes here</p></div>
  </section>
  <section class="sheet slide col-c row-1">
    <h3>Welcome to our Presentation</h3>
    <div class="body"><ul><li>First topic item</li><li>Second topic item</li><li>Third topic item</li></ul></div>
  </section>

  <section class="sheet slide col-a row-2">
    <h3>Heading Here</h3>
    <div class="image-slot" style="left:8px;top:24px;width:42px;height:34px" role="img" aria-label="Placeholder for a slide image"></div>
    <div class="body" style="top:62px"><p>Text here</p></div>
  </section>
  <section class="sheet slide col-b row-2">
    <h3>Heading Here</h3>
    <svg class="chart" width="116" height="78" viewBox="0 0 116 78" role="img" aria-label="Bar chart">
      <line x1="0" y1="76" x2="116" y2="76" stroke="#9aa0a4" stroke-width=".6"/>
      <rect x="8" y="46" width="15" height="30" fill="#1f5f8b"/>
      <rect x="35" y="24" width="15" height="52" fill="#1f5f8b"/>
      <rect x="62" y="52" width="15" height="24" fill="#1f5f8b"/>
      <rect x="89" y="12" width="15" height="64" fill="#1f5f8b"/>
    </svg>
  </section>
  <section class="sheet slide col-c row-2">
    <h3>Agenda</h3>
    <div class="body"><ol><li>Introduction</li><li>Our services</li><li>Cloud solutions</li><li>Contact us</li></ol></div>
  </section>

</body>
</html>
```